【依頼の目的/概要】
電子書籍(lumora)の表紙デザインをお願いします。

【画像サイズ】※RXMより抜粋
表紙ファイルの理想的な寸法は2,560×1,600ピクセルです。
注:画像の寸法は1,000×625ピクセル以上であることが必要です。
画像の最大の寸法は10,000×10,000ピクセルです。

【タイトル】
黄金のレシピ
-10歳!本当の美しさに出会える魔法

【サブタイトル】
あなたは幸せ顔?診断テストが満載!
症状別に冷え・食・香りで解決!

【著者】
美容経歴20年以上・小学生~80歳のお悩み解決5000人以上
トータル美容アドバイザー:森川ゆかり(ブルームリーフ代表)

【本の内容】
この本は食生活・隠れ冷えなどを改善し、精油の力で美容健康に
導く本です。
ご自分の今の状態が解り、それぞれの不調・悩みを改善する
診断テストが盛りだくさんです。
以下に本の目次を書き出しました。
原稿も添付ファイルしますので宜しくお願いします。

第1章|真の美しさを引き出す土台づくり
◆気・血・水のバランスを整える
◆気・血・水のタイプ別:特徴
◆気・血・水のタイプ別:改善策
◆木・火・土・金・水
五行説で心身の弱点を診断
◆五行の診断テスト
◆五行別:改善策

第2章|美肌になるための食べ物
◆腸内環境を整えるオススメ食品
◆美肌になる食べ物

第3章|隠れ冷えを改善して、免疫力UP
◆あなたの体の「冷え」はどのタイプ?
◆各タイプ別:改善策

第4章|今日から簡単に取り入れられる!
お悩み別!美容の裏ワザQ&A
◆Q1:かかとのガサガサ、どうにかしたい!
◆Q2:何だか最近、顔がくすんでみえます・・・
◆Q3:お顔のたるみ、年のせいだから仕方ない?
◆Q4:爪が割れやすくなってきました・・・
◆Q5:お肌の乾燥が気になります!
◆Q6:タルミに効果的なマッサージは?
◆Q7:冬の紫外線対策って必要ですか?
◆Q8:年々、白髪や薄毛が気になります・・・
◆Q9:マスカラをキレイに塗りたい!
◆Q10:眉を早くキレイに描きたい!
◆Q11:正しいクレンジング方法は?

第5章|香りのある暮らし
精油の活用法&最新情報
◆皮脳同根の原理で脳ストレスを減らそう
◆精油を買う時のポイント
◆好きな香りで作る芳香剤
◆更年期にオススメの精油活用法
◆吸収のメカニズム・香りの経路
◆レジリエンスを高める4つのレッスン
◆あなたにぴったりな香りはどれ?
◆知られざる精油の効果・効能

【デザイン要望】
表紙のイラストは添付しますので、そのイラストを
使ってください。(ミストの女性)

デザインはご自由な発想でお願いします。

文字はタイトル、サブタイトル、著者を入れてください。

次点・次々点の方への参加報酬を設定いたしました。
ご応募を楽しみにお待ちしております。
その他何かご不明な点がございましたら、お気軽にご質問下さい。
よろしくお願いいたします。

この度は素晴らしいデザインをして頂きありがとうございました。
一目でパッと目につき、タイトル文字もはっきりしていて優しい
色合いにとても惹かれました。
何度も修正して頂きありがとうございます。

皆様、この度は素晴らしい沢山のご提案をありがとうございました。
お一人お一人にお礼を申し上げることができませんが、この場をお借りして
お礼申し上げます。本当に皆様お忙しい中ありがとうございました。

```html
<!DOCTYPE html>
<html lang="ja">
<head>
<meta charset="UTF-8">
<title>黄金のレシピ 表紙</title>
<link href="https://fonts.googleapis.com/css2?family=Shippori+Mincho+B1:wght@600;800&family=Noto+Sans+JP:wght@500;700;900&display=swap" rel="stylesheet">
<style>
  :root {
    --bg-center: #fff6f8;
    --bg-edge: #f3b9c9;
    --title-pink: #e0609a;
    --accent-pink: #e8488a;
    --deep-red: #c8144e;
    --ink: #3a2a30;
    --frame: #c4529a;
    --mirror-fill-a: #fbe9ee;
    --mirror-fill-b: #f2c7d2;
    --white: #ffffff;
  }
  * { margin: 0; padding: 0; box-sizing: border-box; }
  html, body { width: 751px; height: 1200px; overflow: hidden; }
  body { font-family: "Noto Sans JP", sans-serif; color: var(--ink); }

  .cover {
    position: relative;
    width: 751px;
    height: 1200px;
    overflow: hidden;
    background: radial-gradient(ellipse at 50% 45%, var(--bg-center) 0%, #fbdce4 55%, var(--bg-edge) 100%);
  }

  .title-word {
    position: absolute;
    left: 0; width: 100%;
    text-align: center;
    font-family: "Shippori Mincho B1", serif;
    font-weight: 800;
    color: var(--title-pink);
    letter-spacing: 6px;
    -webkit-text-stroke: 3px var(--white);
    paint-order: stroke fill;
    text-shadow: 0 3px 8px rgba(180, 60, 110, 0.25);
    line-height: 1;
    white-space: nowrap;
  }
  .title-top { top: 0; font-size: 150px; }
  .title-bottom { top: 915px; font-size: 165px; letter-spacing: 24px; }

  .minus-age {
    position: absolute;
    left: 180px; top: 160px;
    font-weight: 900;
    font-size: 58px;
    color: var(--deep-red);
    line-height: 1;
    white-space: nowrap;
  }
  .minus-age .ruby {
    position: absolute;
    left: 4px; top: -16px;
    font-size: 13px;
    font-weight: 700;
    letter-spacing: 1px;
  }
  .tagline {
    position: absolute;
    left: 388px; top: 150px;
    font-weight: 900;
    font-size: 36px;
    line-height: 1.22;
    color: var(--ink);
    white-space: nowrap;
  }

  .happy-face {
    position: absolute;
    left: 70px; top: 285px;
    width: 150px;
    font-family: "Shippori Mincho B1", serif;
    font-weight: 600;
    font-size: 26px;
    line-height: 1.25;
    color: var(--accent-pink);
    transform: rotate(-14deg);
    text-align: center;
  }
  .happy-face::before {
    content: "";
    position: absolute;
    left: -16px; top: -18px;
    width: 180px; height: 112px;
    border: 2px solid var(--accent-pink);
    border-radius: 50%;
    opacity: 0.6;
  }

  .test-badge {
    position: absolute;
    left: 552px; top: 322px;
    width: 180px;
    padding: 8px 6px 10px;
    background: var(--white);
    border: 3px solid var(--deep-red);
    border-radius: 14px;
    text-align: center;
    color: var(--deep-red);
    font-weight: 900;
    line-height: 1.2;
    white-space: nowrap;
  }
  .test-badge .big { font-size: 32px; display: block; }
  .test-badge .small { font-size: 22px; }

  .mirror {
    position: absolute;
    left: 250px; top: 236px;
    width: 280px; height: 420px;
  }

  .solution {
    position: absolute;
    left: 0; top: 652px; width: 100%;
    text-align: center;
    font-weight: 900;
    font-size: 40px;
    color: var(--deep-red);
    letter-spacing: 1px;
    white-space: nowrap;
  }
  .solution .hl {
    display: inline-block;
    background: var(--accent-pink);
    color: var(--white);
    padding: 0 10px;
    margin: 0 4px;
    border-radius: 6px;
    font-size: 46px;
  }

  .credentials {
    position: absolute;
    left: 40px; top: 730px;
    width: 300px;
    list-style: none;
  }
  .credentials li {
    background: var(--accent-pink);
    color: var(--white);
    font-weight: 700;
    font-size: 19px;
    line-height: 1.3;
    padding: 6px 10px 6px 34px;
    border-radius: 8px;
    margin-bottom: 8px;
    position: relative;
    white-space: nowrap;
  }
  .credentials li::before {
    content: "";
    position: absolute;
    left: 11px; top: 12px;
    width: 14px; height: 14px;
    border: 3px solid var(--white);
    border-radius: 50%;
  }

  .author {
    position: absolute;
    left: 370px; top: 718px;
    width: 355px;
    text-align: center;
    color: var(--ink);
    white-space: nowrap;
  }
  .author .role { font-weight: 700; font-size: 22px; }
  .author .name {
    font-family: "Shippori Mincho B1", serif;
    font-weight: 800;
    font-size: 58px;
    letter-spacing: 4px;
    line-height: 1.15;
  }
  .author .org { font-weight: 700; font-size: 21px; }
</style>
</head>
<body>
  <main class="cover">
    <h1 class="title-word title-top">黄金の</h1>

    <div class="minus-age"><span class="ruby">マイナス</span>−10歳!</div>
    <p class="tagline">本当の美しさに<br>出会える魔法</p>

    <p class="happy-face">あなたは<br>幸せ顔?</p>

    <svg class="mirror" viewBox="0 0 280 420">
      <defs>
        <linearGradient id="mirrorFill" x1="0" y1="0" x2="0" y2="1">
          <stop offset="0" stop-color="#fbe9ee"/>
          <stop offset="1" stop-color="#f2c7d2"/>
        </linearGradient>
      </defs>
      <ellipse cx="140" cy="210" rx="132" ry="202" fill="none" stroke="#c4529a" stroke-width="10"/>
      <ellipse cx="140" cy="210" rx="120" ry="190" fill="url(#mirrorFill)" role="img" aria-label="鏡の中でミストを吹きかける女性のイラスト"/>
      <ellipse cx="140" cy="210" rx="120" ry="190" fill="none" stroke="#ffffff" stroke-width="3"/>
    </svg>

    <div class="test-badge"><span class="big">診断テスト</span><span class="small">が満載!</span></div>

    <p class="solution">症状別に<span class="hl">冷え・食・香り</span>で解決!</p>

    <ul class="credentials">
      <li>美容経歴20年以上</li>
      <li>小学生〜80歳のお悩み解決<br>5000人以上</li>
    </ul>

    <div class="author">
      <p class="role">トータル美容アドバイザー</p>
      <p class="name">森川ゆかり</p>
      <p class="org">(ブルームリーフ代表)</p>
    </div>

    <p class="title-word title-bottom">レシピ</p>
  </main>
</body>
</html>
```